Business card, postcard, pocket folder

We are a real estate team and have had a new logo designed. From this, we need the following deliverables:- Business Cards (double-sided)- Just Listed / Just Sold Postcards (double-sided)- Pocket Folder. See logo attached.More work possible for the winning designer.
There are 5 members of the team, so head shots should be easily changed and possible for a group photo might be a good idea for the pocket folder but not 100% neccessary.
Target Market(s)
Real estate
Industry/Entity Type
Real Estate
Font styles to use
Serif
Sans Serif
Requirements
Must have
- Business cards and postcards must have a head shot on them.

```html
<!DOCTYPE html>
<html lang="en">
<head>
<meta charset="UTF-8">
<title>Harrowgate Group – Business Card</title>
<link rel="stylesheet" href="https://fonts.googleapis.com/css2?family=Open+Sans:wght@400;600;700&display=swap">
<style>
  :root {
    --backdrop: #2a2a2c;
    --card-white: #ffffff;
    --brand-blue: #22389a;
    --ink-grey: #5a5a5a;
    --photo-dark: #3a3a36;
    --photo-light: #e9e9e6;
    --rule-white: #ffffff;
  }
  * { margin: 0; padding: 0; box-sizing: border-box; }
  html, body {
    width: 1200px; height: 892px; overflow: hidden;
    background: var(--backdrop);
    font-family: "Open Sans", Arial, sans-serif;
  }
  .canvas {
    position: relative; width: 1200px; height: 892px;
  }
  .card {
    position: absolute; width: 620px; height: 354px;
    background: var(--card-white);
    box-shadow: 0 10px 28px rgba(0,0,0,0.45);
    overflow: hidden;
  }
  .card--front { left: 290px; top: 40px; }
  .card--back { left: 290px; top: 480px; display: flex; }

  /* Front */
  .brand {
    position: absolute; left: 0; right: 0; top: 128px;
    text-align: center;
  }
  .brand__name {
    font-weight: 700; font-size: 50px; color: var(--brand-blue);
    letter-spacing: -0.5px; line-height: 1;
  }
  .website {
    position: absolute; left: 0; right: 0; bottom: 62px;
    text-align: center; font-size: 15px; color: var(--ink-grey);
    letter-spacing: 6px;
  }

  /* Back */
  .headshot {
    width: 300px; height: 100%;
    background: linear-gradient(160deg, var(--photo-light) 0%, #bdbdb8 45%, var(--photo-dark) 100%);
  }
  .details {
    flex: 1; background: var(--brand-blue); color: #fff;
    display: flex; flex-direction: column; align-items: center;
    justify-content: center; text-align: center; padding: 0 20px;
  }
  .details__name { font-weight: 700; font-size: 22px; letter-spacing: 0.3px; line-height: 1.1; }
  .details__role { font-size: 15px; letter-spacing: 0.5px; }
  .details__rule {
    width: 70px; height: 1px; background: var(--rule-white);
    margin: 20px 0;
  }
  .details__address { font-size: 15px; line-height: 1.4; }
  .details__contact { font-size: 15px; line-height: 1.5; }
  .details__contact b { font-weight: 700; }
</style>
</head>
<body>
<main class="canvas">
  <section class="card card--front" aria-label="Business card front">
    <div class="brand">
      <div class="brand__name">Harrowgate Group</div>
    </div>
    <div class="website">www.harrowgate.com</div>
  </section>

  <section class="card card--back" aria-label="Business card back">
    <div class="headshot" role="img" aria-label="Head shot of team member in suit and tie"></div>
    <div class="details">
      <div class="details__name">MARK ELLISON</div>
      <div class="details__role">PRESIDENT</div>
      <div class="details__rule"></div>
      <div class="details__address">2716 Alder Crest Lane<br>Millbrook, NY 12545</div>
      <div class="details__rule"></div>
      <div class="details__contact">
        <b>P:</b> 555 0142 2871 <b>M:</b> 555 0198 4410<br>
        <b>E:</b> mark@harrowgate.com
      </div>
    </div>
  </section>
</main>
</body>
</html>
```